I need creative and unique business card design using my company logo. Ok to change logo color. We are a small brokerage doing both Real Estate and Mortgage services. Need to have the follow on business card;
1. agent name - Mila Fenton - Realtor
2. cell - 949-555-0182
3. license number - DRE 04917362
4. business name - Brightway Estates & Lending, Inc
5. business office - 626-555-0147
6. business address - 287 W. Larkmoor Ave #214, Arcadia CA 91088
7. business logo - attached (ok to use different color on logo)

```html
<!DOCTYPE html>
<html lang="en">
<head>
<meta charset="utf-8">
<title>Brightway Estates &amp; Lending – Business Card</title>
<link href="https://fonts.googleapis.com/css2?family=Montserrat:wght@400;500;700&display=swap" rel="stylesheet">
<style>
  :root {
    --stage: #e9ecf1;
    --brand-blue: #2e5fae;
    --brand-blue-deep: #2a58a8;
    --brand-blue-light: #4fa3dc;
    --ink: #555a61;
    --card-white: #ffffff;
  }
  html, body {
    margin: 0;
    width: 1200px;
    height: 913px;
    overflow: hidden;
    background: var(--stage);
    font-family: "Montserrat", Arial, sans-serif;
  }
  .stage {
    position: relative;
    width: 1200px;
    height: 913px;
    display: flex;
    flex-direction: column;
    align-items: center;
    justify-content: center;
    gap: 56px;
  }
  .card {
    width: 620px;
    height: 354px;
    border-radius: 22px;
    position: relative;
    overflow: hidden;
    box-shadow: 0 10px 28px rgba(20, 40, 80, 0.18);
  }
  /* Front */
  .card--front {
    background: radial-gradient(circle at 55% 55%, var(--brand-blue-light) 0%, #3f86cc 45%, var(--brand-blue-deep) 100%);
    display: flex;
    align-items: center;
    justify-content: center;
  }
  .front-name {
    color: #ffffff;
    font-weight: 500;
    font-size: 22px;
    letter-spacing: 0.28em;
    text-transform: uppercase;
    text-align: center;
    line-height: 1.5;
    margin: 0;
  }
  /* Back */
  .card--back {
    background: var(--card-white);
    display: grid;
    grid-template-columns: 300px 1px 1fr;
    align-items: center;
  }
  .brand {
    display: flex;
    flex-direction: column;
    align-items: center;
    gap: 22px;
    padding-left: 20px;
  }
  .brand-square {
    width: 96px;
    height: 96px;
    background: var(--brand-blue);
  }
  .brand-name {
    color: var(--brand-blue);
    font-weight: 500;
    font-size: 14px;
    letter-spacing: 0.22em;
    text-transform: uppercase;
    text-align: center;
    line-height: 1.6;
    margin: 0;
  }
  .divider {
    width: 1px;
    height: 150px;
    background: var(--brand-blue);
  }
  .contact {
    padding-left: 34px;
    color: var(--ink);
    font-size: 15px;
    line-height: 1.5;
  }
  .agent-name {
    color: var(--brand-blue);
    font-weight: 700;
    font-size: 22px;
    margin: 0;
    letter-spacing: 0.01em;
    text-transform: uppercase;
  }
  .agent-role { margin: 0 0 4px; font-size: 15px; }
  .line { margin: 0; display: flex; align-items: center; gap: 8px; }
  .line svg { width: 14px; height: 14px; flex: none; }
  .license { color: var(--brand-blue); font-weight: 700; margin: 2px 0; }
  .address { margin: 4px 0 0; }
</style>
</head>
<body>
<main class="stage">
  <section class="card card--front">
    <p class="front-name">Brightway<br>Estates &amp; Lending, Inc</p>
  </section>

  <section class="card card--back">
    <div class="brand">
      <div class="brand-square"></div>
      <p class="brand-name">Brightway<br>Estates &amp; Lending, Inc</p>
    </div>
    <div class="divider"></div>
    <div class="contact">
      <h1 class="agent-name">Mila Fenton</h1>
      <p class="agent-role">Realtor</p>
      <p class="line">
        <svg viewBox="0 0 14 14" aria-hidden="true"><rect x="3.5" y="1" width="7" height="12" rx="1.5" fill="none" stroke="var(--brand-blue)" stroke-width="1.3"/><line x1="6" y1="11" x2="8" y2="11" stroke="var(--brand-blue)" stroke-width="1.2"/></svg>
        949-555-0182
      </p>
      <p class="address">287 W. Larkmoor Ave<br>#214, Arcadia CA 91088</p>
      <p class="license">DRE 04917362</p>
      <p class="line">
        <svg viewBox="0 0 14 14" aria-hidden="true"><path d="M3 1.5 L5.2 1.5 L6 4.5 L4.6 5.6 C5.3 7.3 6.7 8.7 8.4 9.4 L9.5 8 L12.5 8.8 L12.5 11 C12.5 12 11.6 12.6 10.6 12.5 C5.8 12 2 8.2 1.5 3.4 C1.4 2.4 2 1.5 3 1.5 Z" fill="var(--brand-blue)"/></svg>
        626-555-0147
      </p>
    </div>
  </section>
</main>
</body>
</html>
```